Accounting practice seeks business card redesign with existing logo

Accounting practice has logo and slogan but more needs modern professional business revision. Must be in a file format ready to print quality business cards.

Open to artistic ideas but for the brand recognition the features below must be incorporated:

- Logo: attached in EPS format (Logo now blue)
- Slogan: Proven Business Solutions... That Work! (in orange legible handwriting type font)
- Name: Dorian T Felsham RBA AAT JP (letters in smaller font)
- Phone icon: 1800 593 817
- Mobile phone icon: 0488 614 752
- Web icon: www.velprasolutions.com.au
- Email icon: admin@velprasolutions.com.au
- See pics for dark blue/med blue line at bottom, this is a necessity.
- Globe that forms the 'dot' in the 'I' of Velpra is attached. It is too big at present.
- Rear side: pic attached. Note my logo is a watermark. I Will provide slightly revised wording details later. Please allow for a small white space at bottom of rear of card to write notes/appointment details.

I am open to ideas but must retain the above for brand recognition.

```html
<!DOCTYPE html>
<html lang="en">
<head>
<meta charset="utf-8">
<title>Velpra Solutions – Business Card</title>
<link rel="stylesheet" href="https://fonts.googleapis.com/css2?family=Open+Sans:wght@400;600&display=swap">
<style>
  :root {
    --navy: #1b2a5c;
    --navy-soft: #26386f;
    --sky: #5ab0d8;
    --pill: #1c78bb;
    --white: #ffffff;
    --ink: #111111;
    --backdrop: #e8e6e2;
  }
  * { box-sizing: border-box; margin: 0; padding: 0; }
  html, body { width: 1200px; height: 1200px; overflow: hidden; }
  body {
    background: var(--backdrop);
    font-family: "Open Sans", Arial, sans-serif;
    position: relative;
  }
  .card {
    position: absolute;
    width: 760px;
    height: 460px;
    overflow: hidden;
    box-shadow: 0 6px 18px rgba(0,0,0,.18);
  }
  .card-front { left: 60px; top: 70px; background: var(--white); }
  .card-back { left: 380px; top: 660px; background: var(--navy); }
  .card-shapes { position: absolute; inset: 0; }

  /* front */
  .brand {
    position: absolute; left: 0; right: 0; top: 70px;
    display: flex; align-items: center; justify-content: center; gap: 14px;
    color: var(--sky); font-size: 46px; font-weight: 400; letter-spacing: 4px;
  }
  .brand-dot { width: 26px; height: 26px; border-radius: 50%; background: var(--sky); }
  .holder { position: absolute; left: 150px; top: 232px; color: var(--navy); }
  .holder-name { font-size: 36px; font-weight: 400; }
  .holder-role { font-size: 24px; color: var(--ink); margin: 4px 0 0 190px; }
  .contacts { position: absolute; display: flex; flex-direction: column; gap: 10px; }
  .contacts-phone { left: 70px; top: 352px; }
  .contacts-web { left: 320px; top: 336px; }
  .pill {
    display: flex; align-items: center; gap: 10px;
    background: var(--pill); color: var(--white);
    border-radius: 16px; height: 30px; padding: 0 18px 0 4px;
    font-size: 17px;
  }
  .pill-icon {
    width: 24px; height: 24px; border-radius: 50%;
    background: var(--white); display: flex; align-items: center; justify-content: center;
  }

  /* back */
  .watermark {
    position: absolute; left: 130px; top: 170px;
    color: var(--navy-soft); font-size: 92px; letter-spacing: 10px; font-weight: 400;
  }
  .intro {
    position: absolute; left: 44px; top: 40px; width: 640px;
    color: var(--white); font-size: 23px; line-height: 1.3;
  }
  .services { position: absolute; list-style: none; color: var(--white); font-size: 23px; }
  .services li { margin-bottom: 18px; }
  .services-left { left: 80px; top: 200px; }
  .services-right { left: 420px; top: 150px; }
  .services-right li { margin-bottom: 10px; }
  .notes-strip { position: absolute; left: 0; right: 0; bottom: 0; height: 58px; background: var(--white); }
</style>
</head>
<body>

<section class="card card-front" aria-label="Business card front">
  <svg class="card-shapes" viewBox="0 0 760 460" aria-hidden="true">
    <rect x="0" y="0" width="760" height="200" fill="var(--navy)"/>
    <polygon points="0,0 120,0 0,170" fill="var(--white)"/>
    <polygon points="0,110 80,0 110,0 0,150" fill="var(--sky)"/>
    <polygon points="0,170 120,0 130,0 0,200" fill="var(--white)"/>
    <polygon points="0,215 70,200 0,240" fill="var(--navy)"/>
    <polygon points="760,250 760,460 560,460" fill="var(--navy)"/>
    <polygon points="760,215 760,245 630,420 600,420" fill="var(--sky)"/>
    <polygon points="760,330 760,360 690,460 660,460" fill="var(--sky)"/>
  </svg>

  <div class="brand"><span class="brand-dot"></span><span>Velpra Solutions</span></div>

  <div class="holder">
    <p class="holder-name">Dorian T Felsham RBA AAT JP</p>
    <p class="holder-role">PRINCIPAL</p>
  </div>

  <div class="contacts contacts-phone">
    <div class="pill">
      <span class="pill-icon"><svg width="14" height="14" viewBox="0 0 14 14"><path d="M2 4c0-2 3-2 3-1v2L4 6c1 2 2 3 4 4l1-1h2c1 0 1 3-1 3C6 12 2 8 2 4z" fill="var(--pill)"/></svg></span>
      <span>1800 593 817</span>
    </div>
    <div class="pill">
      <span class="pill-icon"><svg width="14" height="14" viewBox="0 0 14 14"><rect x="4" y="1" width="6" height="12" rx="1.2" fill="none" stroke="var(--pill)" stroke-width="1.6"/></svg></span>
      <span>0488 614 752</span>
    </div>
  </div>

  <div class="contacts contacts-web">
    <div class="pill">
      <span class="pill-icon"><svg width="14" height="14" viewBox="0 0 14 14"><circle cx="7" cy="7" r="5.5" fill="none" stroke="var(--pill)" stroke-width="1.4"/><path d="M1.5 7h11M7 1.5c-3 3-3 8 0 11M7 1.5c3 3 3 8 0 11" fill="none" stroke="var(--pill)" stroke-width="1.1"/></svg></span>
      <span>www.velprasolutions.com.au</span>
    </div>
    <div class="pill">
      <span class="pill-icon"><svg width="14" height="14" viewBox="0 0 14 14"><rect x="1.5" y="3" width="11" height="8" fill="none" stroke="var(--pill)" stroke-width="1.4"/><path d="M1.5 3l5.5 4.5L12.5 3" fill="none" stroke="var(--pill)" stroke-width="1.2"/></svg></span>
      <span>admin@velprasolutions.com.au</span>
    </div>
  </div>
</section>

<section class="card card-back" aria-label="Business card back">
  <svg class="card-shapes" viewBox="0 0 760 460" aria-hidden="true">
    <polygon points="760,270 760,300 690,400 660,400" fill="var(--sky)"/>
    <polygon points="760,330 760,402 700,402 705,395" fill="var(--white)"/>
    <polygon points="760,340 760,370 740,402 710,402" fill="var(--sky)"/>
  </svg>
  <div class="watermark">Velpra Solutions</div>
  <p class="intro">You trusted provider of quality business and accounting solutions, proven to work for small to mediuim business and trades.</p>
  <ul class="services services-left">
    <li>Bookkeeping</li>
    <li>BAS</li>
    <li>Cloud Accounting</li>
    <li>Debt Recovery</li>
  </ul>
  <ul class="services services-right">
    <li>Business Advice</li>
    <li>ATO Assistance</li>
    <li>Office Technology</li>
    <li>And Much More...</li>
  </ul>
  <div class="notes-strip"></div>
</section>

</body>
</html>
```